Camp Thornbriar Retreat Brochure

I'm looking for someone who can design a brochure for our organization. We a Christian camp and retreat center. The brochure will be to help us attract more rentals. I have attached a word document with the information that will need to be included on each page. Below you will also find a link to google drive that will need to be included. I would like it to be 11 (L) x 17 (W) before the fold, it will be a half fold. The page will need to be bleed so it won't have white edges. It will also need CMYK color mode done. I included several pictures for the inside, not sure if they will all fit, but would like to include several if it looks good.https://files.vexlora.net/open?id=7kQpRtZ2mXbLwN9cVhYa4DsEeGuJoFi3

Target Market(s)

Organizations that might be interested in renting our facility. Church groups, civic organizations, schools, weddings, etc.

Industry/Entity Type

Hospitality

Font styles to use
Serif
Sans Serif

Colors

Designer to choose colors to be used in the design.

Requirements
Must have
• Information listed in the word document I provided. Pictures that I provided, may have provided too many.
Nice to have
• Nice graphics. Creative designs. I really have no idea. I'm horrible at this stuff.
Should not have
• Not sure

```html
<!DOCTYPE html>
<html lang="en">
<head>
<meta charset="utf-8">
<title>Retreats at Thornbriar – Brochure</title>
<link rel="stylesheet" href="https://fonts.googleapis.com/css2?family=Playfair+Display:wght@700;900&family=Nunito+Sans:wght@300;400;700;800&display=swap">
<style>
:root{
  --bg:#a9a9ab;
  --plum:#6b1d52;
  --plum-deep:#55103f;
  --plum-soft:#8a3a70;
  --red:#d42a3c;
  --paper:#f1f1f1;
  --paper-grey:#e4e4e5;
  --ink:#3a2a35;
  --white:#ffffff;
}
*{box-sizing:border-box;margin:0;padding:0}
html,body{width:989px;height:1200px;overflow:hidden;background:var(--bg)}
body{position:relative;font-family:"Nunito Sans",Arial,sans-serif;color:var(--ink)}
.page{position:absolute;overflow:hidden;box-shadow:0 4px 10px rgba(0,0,0,.25)}

/* cover */
.cover{left:130px;top:96px;width:359px;height:464px;background:#2a2318}
.cover-photo{position:absolute;inset:0;background:
  radial-gradient(ellipse 140px 70px at 300px 175px,rgba(255,214,140,.95),rgba(255,190,110,0) 100%),
  radial-gradient(ellipse 90px 260px at 350px 250px,rgba(40,34,20,.85),rgba(40,34,20,0) 100%),
  radial-gradient(ellipse 160px 90px at 170px 330px,rgba(90,40,50,.55),rgba(90,40,50,0) 100%),
  radial-gradient(ellipse 260px 90px at 180px 440px,rgba(22,18,14,.95),rgba(22,18,14,0) 100%),
  linear-gradient(180deg,#f6eedf 0%,#f0dcb4 22%,#e2b476 38%,#9c7a42 47%,#6f6a36 55%,#4d4a27 66%,#3a3320 78%,#221c14 100%)}
.brand{position:absolute;left:22px;top:52px;width:318px;color:var(--plum);font-weight:800}
.brand-small{font-size:19px;text-align:right;display:block;padding-right:8px}
.brand-main{font-size:58px;line-height:1;letter-spacing:-1.5px;display:block;margin-top:-2px}
.cover-url{position:absolute;left:0;right:0;bottom:29px;text-align:center;color:var(--white);font-size:9.5px;letter-spacing:2.6px}
.cover-rule{position:absolute;left:0;right:0;bottom:16px;height:1px;background:var(--red)}

/* back */
.back{left:520px;top:96px;width:360px;height:464px;background:linear-gradient(180deg,#6e2458,var(--plum) 60%,#5e1848)}
.back-photo{position:absolute;left:0;top:0;width:100%;height:240px;background:
  radial-gradient(ellipse 90px 60px at 70px 40px,rgba(190,50,90,.75),rgba(190,50,90,0) 100%),
  radial-gradient(ellipse 110px 50px at 230px 60px,rgba(170,40,80,.7),rgba(170,40,80,0) 100%),
  radial-gradient(ellipse 70px 60px at 270px 150px,rgba(60,20,45,.8),rgba(60,20,45,0) 100%),
  linear-gradient(90deg,rgba(70,20,50,0) 0,rgba(70,20,50,.5) 20%,rgba(70,20,50,0) 24%,rgba(70,20,50,0) 34%,rgba(70,20,50,.5) 38%,rgba(70,20,50,0) 42%),
  linear-gradient(180deg,#94386a 0%,#86305f 45%,#7c2d5c 70%,rgba(107,29,82,0) 100%)}
.back-rule-v{position:absolute;left:18px;top:0;bottom:0;width:1px;background:rgba(212,42,60,.55)}
.back-rule-h{position:absolute;left:0;right:0;bottom:10px;height:1px;background:rgba(212,42,60,.45)}
.contact-icons{position:absolute;left:0;right:0;top:318px;display:flex;justify-content:center;gap:4px;margin-left:-232px;width:592px}
.contact-icons{left:-40px}
.contact-box{position:absolute;left:36px;top:242px;width:180px;height:107px;border:1px solid var(--red);text-align:center;color:#f1dbe8;font-weight:300;font-size:10px;line-height:13.6px;padding-top:14px}
.contact-box strong{display:block;color:var(--white);font-weight:700;font-size:10.6px;letter-spacing:.3px;margin-bottom:1px}
.icons{position:absolute;left:0;width:252px;top:230px;display:flex;justify-content:center;gap:4px}
.icons svg{width:14px;height:14px}
.events-pill{position:absolute;left:87px;top:362px;width:80px;height:17px;border-radius:9px;background:var(--white);color:var(--plum);font-weight:700;font-size:10px;text-align:center;line-height:17px}
.events-list{position:absolute;left:40px;top:385px;width:220px;display:grid;grid-template-columns:111px 109px;row-gap:3px;list-style:none;color:#f1dbe8;font-size:7.2px;font-weight:300}
.events-list li::before{content:"";display:inline-block;width:5px;height:5px;border-radius:50%;background:var(--red);margin-right:5px}

/* spread */
.spread{left:133px;top:596px;width:745px;height:500px;background:var(--paper)}
.left-head{position:absolute;left:0;top:0;width:369px;height:196px;background:linear-gradient(135deg,var(--plum-soft),var(--plum) 50%,var(--plum-deep))}
.left-head h2{position:absolute;left:21px;top:38px;font-family:"Playfair Display",serif;font-weight:900;color:var(--white);font-size:34px;line-height:37px;letter-spacing:-.3px}
.left-head p{position:absolute;left:23px;top:116px;color:var(--white);font-weight:300;font-size:14.6px;line-height:19.5px}
.left-head .dash{position:absolute;left:23px;top:166px;width:18px;height:2px;background:var(--red)}
.right-photo{position:absolute;left:369px;top:0;width:376px;height:196px;background:
  radial-gradient(ellipse 40px 30px at 138px 115px,rgba(25,15,10,.9),rgba(25,15,10,0) 100%),
  linear-gradient(180deg,rgba(0,0,0,0) 0,rgba(0,0,0,0) 60%,rgba(200,170,150,.55) 78%,rgba(220,205,195,.8) 100%),
  linear-gradient(90deg,#4b3a30 0%,#6b5646 18%,#5a4a3e 36%,#9a6436 44%,#b9773c 58%,#a86c38 66%,#c98f55 78%,#b98150 88%,#d9b791 100%)}
.ring{position:absolute;left:292px;top:-6px;width:166px;height:166px;border-radius:50%;background:var(--plum);box-shadow:0 0 0 2px rgba(255,255,255,.35) inset}
.ring-photo{position:absolute;left:302px;top:4px;width:146px;height:146px;border-radius:50%;background:
  linear-gradient(180deg,rgba(0,0,0,0) 0,rgba(0,0,0,0) 54%,#a07a5a 58%,#7c5a40 66%,rgba(0,0,0,0) 67%),
  linear-gradient(180deg,#5f8f45 0%,#3f6f30 35%,#5b8a44 52%,#6f8f55 66%,#b8b2a4 76%,#9a968c 100%)}
.badge{position:absolute;left:490px;top:100px;width:138px;height:138px;border-radius:50%;background:#ebe8ea;border:3px solid var(--white);box-shadow:0 2px 6px rgba(0,0,0,.2);display:flex;align-items:center;justify-content:center;text-align:center}
.badge::after{content:"";position:absolute;inset:5px;border-radius:50%;border:1px dotted #b9a9b4}
.badge h3{font-family:"Playfair Display",serif;font-weight:900;color:var(--plum);font-size:17.5px;line-height:22.5px}
.lower-left{position:absolute;left:0;top:196px;width:369px;height:304px;background:var(--paper-grey)}
.amenities{position:absolute;list-style:none;font-size:8.4px;color:var(--ink)}
.amenities li{position:relative;padding-left:13px;margin-bottom:7.8px;line-height:10px}
.amenities li.tick::before{content:"";position:absolute;left:0;top:1px;width:7px;height:7px;border:1px solid var(--plum);border-radius:50%}
.amenities li.tick::after{content:"";position:absolute;left:2px;top:3px;width:3px;height:1.6px;border-left:1px solid var(--red);border-bottom:1px solid var(--red);transform:rotate(-45deg)}
.amenities li.dot::before{content:"";position:absolute;left:2px;top:4px;width:3px;height:3px;border-radius:50%;background:var(--ink)}
.amenities .cap{font-weight:800;text-transform:uppercase;font-size:8px}
.photo{position:absolute}
.bunk-tall{left:237px;top:18px;width:114px;height:246px;background:
  radial-gradient(ellipse 40px 8px at 20px 8px,rgba(255,255,255,.7),rgba(255,255,255,0)),
  linear-gradient(90deg,rgba(0,0,0,0) 0,rgba(0,0,0,0) 55%,rgba(180,110,50,.7) 60%,rgba(0,0,0,0) 66%,rgba(0,0,0,0) 80%,rgba(170,100,45,.7) 84%,rgba(0,0,0,0) 88%),
  linear-gradient(180deg,#a8703c 0%,#c48a4c 18%,#e9e0d0 24%,#d9ccb8 55%,#cfc2ae 72%,#e8e4dc 82%,#d6d2ca 100%)}
.bunk-small{left:17px;top:160px;width:108px;height:102px;background:
  linear-gradient(90deg,rgba(0,0,0,0) 0,rgba(0,0,0,0) 38%,#2a2c3a 40%,#2a2c3a 50%,rgba(0,0,0,0) 52%,rgba(0,0,0,0) 78%,#2a2c3a 80%,#2a2c3a 92%,rgba(0,0,0,0) 94%),
  linear-gradient(180deg,#d8c8ae 0%,#cdb694 40%,#b68d5c 70%,#9c744a 100%)}
.hall{left:127px;top:160px;width:108px;height:102px;background:
  radial-gradient(ellipse 30px 14px at 55px 28px,rgba(255,225,170,.85),rgba(255,225,170,0)),
  linear-gradient(180deg,#7a4a2a 0%,#a66a3c 35%,#6a4026 60%,#3e2a22 100%)}
.footer-line{position:absolute;top:484px;height:1px;background:var(--plum-soft)}
.page-num{position:absolute;top:477px;width:13px;height:13px;border-radius:50%;background:var(--plum);color:var(--white);font-size:8px;font-weight:700;text-align:center;line-height:13px}
.footer-brand{position:absolute;top:471px;color:var(--plum);font-weight:800;font-size:12px}
.avail{position:absolute;left:369px;width:376px;top:258px;text-align:center;color:var(--red);font-weight:300;font-size:13.4px}
.fold{position:absolute;left:368px;top:0;width:4px;height:500px;background:linear-gradient(90deg,rgba(0,0,0,.1),rgba(0,0,0,0))}
</style>
</head>
<body>

<section class="page cover">
  <div class="cover-photo" role="img" aria-label="Photo of a group of campers arm in arm on a rocky overlook at sunset above forested hills"></div>
  <div class="brand"><span class="brand-small">Retreats at</span><span class="brand-main">Thornbriar</span></div>
  <div class="cover-url">WWW.WEBSITEADDRESS.COM</div>
  <div class="cover-rule"></div>
</section>

<section class="page back">
  <div class="back-photo" role="img" aria-label="Photo of a stone pavilion among autumn trees, tinted plum"></div>
  <div class="back-rule-v"></div>
  <div class="back-rule-h"></div>
  <div class="icons">
    <svg viewBox="0 0 14 14"><circle cx="7" cy="7" r="7" fill="#fff"/><path d="M7 3.2a2.4 2.4 0 0 0-2.4 2.4C4.6 7.5 7 10.6 7 10.6s2.4-3.1 2.4-5A2.4 2.4 0 0 0 7 3.2z" fill="#6b1d52"/><circle cx="7" cy="5.6" r=".9" fill="#fff"/></svg>
    <svg viewBox="0 0 14 14"><circle cx="7" cy="7" r="7" fill="#fff"/><path d="M4.6 3.8l1.3-.3.8 1.8-.9.7a5 5 0 0 0 2.2 2.2l.7-.9 1.8.8-.3 1.3c-3 .4-6-2.6-5.6-5.6z" fill="#6b1d52"/></svg>
    <svg viewBox="0 0 14 14"><circle cx="7" cy="7" r="7" fill="#fff"/><circle cx="7" cy="7" r="3.6" fill="none" stroke="#6b1d52" stroke-width=".8"/><path d="M3.4 7h7.2M7 3.4c-1.6 2-1.6 5.2 0 7.2M7 3.4c1.6 2 1.6 5.2 0 7.2" fill="none" stroke="#6b1d52" stroke-width=".6"/></svg>
    <svg viewBox="0 0 14 14"><circle cx="7" cy="7" r="7" fill="#fff"/><rect x="3.8" y="4.6" width="6.4" height="4.8" fill="#6b1d52"/><path d="M3.8 4.6L7 7.3l3.2-2.7" fill="none" stroke="#fff" stroke-width=".7"/></svg>
  </div>
  <div class="contact-box">
    <strong>RETREATS AT THORNBRIAR</strong>
    Creative House Station Road<br>Lorem Reading ABC 123<br>0123 456 7890<br>www.websiteaddress.com<br>info@smailaddress.com
  </div>
  <div class="events-pill">OUR EVENTS</div>
  <ul class="events-list">
    <li>Church Retreats</li><li>Girl Scouts</li>
    <li>Organizational meetings</li><li>School groups</li>
    <li>Boy Scouts</li><li>Weddings</li>
  </ul>
</section>

<section class="page spread">
  <div class="left-head">
    <h2>WALTER M.<br>ASHBY CENTER</h2>
    <p>(AVAILABLE FOR RENTAL<br>AUGUST – MAY)</p>
    <div class="dash"></div>
  </div>
  <div class="right-photo" role="img" aria-label="Photo of a hall interior with a stone fireplace and wood-panelled walls"></div>
  <div class="ring"></div>
  <div class="ring-photo" role="img" aria-label="Photo of the center building among green trees"></div>
  <div class="badge"><h3>ELIAS<br>PENWRIGHT<br>RETREAT<br>CENTER</h3></div>

  <div class="lower-left">
    <ul class="amenities" style="left:18px;top:26px;width:232px">
      <li class="tick">26 Cabins (sleep 10-12)</li>
      <li class="tick">Commercial kitchen and dining hall (seats 150)</li>
      <li class="tick">3 covered pavilions</li>
      <li class="tick">1 covered gym</li>
      <li class="tick">Low and High Ropes Course (available for both sides)</li>
      <li class="tick">Softball and soccer field, sand volleyball, gaga ball pit, fire pit, hiking trails</li>
      <li class="tick">Pool and recreational lake (available June - August</li>
    </ul>
    <div class="photo bunk-tall" role="img" aria-label="Photo of a cabin room with wooden bunk beds"></div>
    <div class="photo bunk-small" role="img" aria-label="Photo of a cabin room with a wooden bunk and windows"></div>
    <div class="photo hall" role="img" aria-label="Photo of a timbered dining hall with chandeliers"></div>
  </div>

  <div class="avail">(AVAILABLE FOR RENTAL ALL YEAR)</div>
  <ul class="amenities" style="left:379px;top:282px;width:180px">
    <li class="tick cap">Retreat Center</li>
    <li class="dot">Enclosed Gym/Meeting Room</li>
    <li class="dot">Dining hall</li>
    <li class="dot">Commercial Kitchen</li>
    <li class="dot">Fireplace</li>
    <li class="dot">11 Upstairs rooms (with full size beds and half baths)</li>
    <li class="dot">2 rooms downstairs (with full size beds/share handicap accessible bathroom)</li>
    <li class="tick cap">4 Large Cabins (sleep 30-40 people)</li>
    <li class="dot" style="margin-top:-4px">Bathrooms located inside the cabins</li>
  </ul>
  <ul class="amenities" style="left:569px;top:282px;width:172px">
    <li class="tick cap" style="margin-bottom:3.4px">Pool (available June – August)</li>
    <li class="tick cap" style="margin-bottom:3.4px">7-Acre Fishing Lake</li>
    <li class="tick cap" style="margin-bottom:3.4px">Fire pit and amphitheater</li>
    <li class="tick cap" style="margin-bottom:3.4px">Small field for activities</li>
    <li class="tick cap" style="margin-bottom:3.4px">1 Covered pavilion</li>
    <li class="tick cap">Horses (available for both sides)</li>
  </ul>

  <div class="fold"></div>
  <div class="page-num" style="left:17px">1</div>
  <div class="footer-line" style="left:32px;width:250px"></div>
  <div class="footer-brand" style="left:290px">Thornbriar</div>
  <div class="footer-brand" style="left:379px">Thornbriar</div>
  <div class="footer-line" style="left:450px;width:262px"></div>
  <div class="page-num" style="left:715px">2</div>
</section>

</body>
</html>
```